Bramwick Client Journey To Success

I need a one-page document that graphically shows the client's journey working with Bramwick from initial assessment to completed project. I want the journey to start at the "basecamp logo" and reach 4 summits (little mountain logos...) .

I'd like the imagery to convey the client starting at basecamp, and moving to each summit. Each summit, should list the subtext under each, as listed on the pdf doc i provided.

The description for the basecamp and 4 summits is attached.

I need the brochure to look like the other brochure that you did for me (attached) .

Target Market(s)

Restaurant Owners

Industry/Entity Type

Construction Management

Font styles to use
Sans Serif

Colors
EB3D1F
EC4F4E
F09395
F8D3D4
FCEDEE

Requirements
Must have
• My logo. Title: Client Journey To Success. Subtitle: The 4 Summits

```html
<!DOCTYPE html>
<html lang="en">
<head>
<meta charset="utf-8">
<title>Bramwick Client Journey To Success</title>
<link rel="stylesheet" href="https://fonts.googleapis.com/css2?family=Montserrat:wght@300;400;500;600;700;800&display=swap">
<style>
  :root{
    --red:#eb3d1f;
    --red-deep:#c8242a;
    --rose:#ec4f4e;
    --pink:#f09395;
    --blush:#f8d3d4;
    --mist:#fcedee;
    --ink:#0b0b0b;
    --paper:#ffffff;
    --page-bg:#efefef;
    --grey:#5a5a5a;
  }
  *{margin:0;padding:0;box-sizing:border-box}
  html,body{width:1200px;height:2402px;overflow:hidden;background:var(--page-bg)}
  body{font-family:"Montserrat",sans-serif;position:relative}
  .brochure{
    position:absolute;left:41px;top:476px;width:860px;height:1115px;
    transform:scale(1.3);transform-origin:0 0;
    background:var(--paper);overflow:hidden;
    box-shadow:0 8px 30px rgba(0,0,0,.18);
  }
  .backdrop{position:absolute;inset:0}
  .brand{position:absolute;left:32px;width:413px;top:200px;display:flex;align-items:center;justify-content:center;gap:10px}
  .brand-mark{width:16px;height:16px;background:var(--red)}
  .brand-name{color:var(--paper);font-weight:800;font-size:15px;letter-spacing:.2px}
  .headline{position:absolute;left:80px;top:282px;color:var(--paper);font-weight:400;font-size:50px;line-height:52px;letter-spacing:-.5px}
  .headline .accent{display:block;color:var(--red);font-weight:800;font-size:54px}
  .stage{position:absolute}
  .stage-title{display:flex;align-items:center;gap:14px;color:var(--red-deep);font-weight:700}
  .basecamp{left:72px;top:462px}
  .basecamp .stage-title{color:var(--red);font-size:38px;gap:20px}
  .badge{width:44px;height:48px;flex:none}
  .stage-list{list-style:none;margin-top:6px}
  .stage-list li{display:flex;align-items:center;gap:12px;font-weight:600}
  .basecamp .stage-list{margin-left:12px}
  .basecamp .stage-list li{color:var(--paper);font-size:21px;line-height:33.5px}
  .tick{width:12px;height:12px;flex:none}
  .summit{left:482px}
  .summit .stage-title{font-size:32px;line-height:30px;align-items:flex-start}
  .summit .stage-title .badge{margin-top:6px}
  .summit-name small{display:block;font-size:22px;font-weight:400;color:var(--ink);line-height:28px;padding-bottom:6px;border-bottom:2px solid var(--red);width:max-content;padding-right:14px}
  .summit .stage-list{margin-left:10px;margin-top:14px}
  .summit .stage-list li{color:var(--ink);font-size:18.5px;line-height:27.6px;font-weight:500}
  .s1{top:52px}.s2{top:330px}.s3{top:540px}.s4{top:772px}
</style>
</head>
<body>
<main class="brochure">
  <svg class="backdrop" viewBox="0 0 860 1115" width="860" height="1115">
    <defs>
      <linearGradient id="sparks" x1="0" y1="0" x2="0" y2="1">
        <stop offset="0" stop-color="#0b0b0b"/>
        <stop offset="1" stop-color="#3a3430"/>
      </linearGradient>
      <linearGradient id="aerial" x1="0" y1="0" x2="1" y2="1">
        <stop offset="0" stop-color="#6f7d86"/>
        <stop offset=".45" stop-color="#3d4a35"/>
        <stop offset=".8" stop-color="#7a5a3a"/>
        <stop offset="1" stop-color="#2d3a3a"/>
      </linearGradient>
      <linearGradient id="crew" x1="0" y1="0" x2="0" y2="1">
        <stop offset="0" stop-color="#ffffff"/>
        <stop offset=".4" stop-color="#e4e4e4"/>
        <stop offset="1" stop-color="#bdbdbd"/>
      </linearGradient>
    </defs>
    <rect width="860" height="1115" fill="var(--paper)"/>
    <rect x="800" y="0" width="60" height="130" fill="var(--blush)" opacity=".7"/>
    <g role="img" aria-label="Grayscale photo of a construction worker in a safety vest">
      <polygon points="600,690 860,690 860,1115 600,1115" fill="url(#crew)"/>
    </g>
    <polygon points="32,0 445,0 445,900 32,690" fill="var(--ink)"/>
    <g role="img" aria-label="Photo of a welder working with sparks flying">
      <polygon points="32,600 445,600 445,900 32,690" fill="url(#sparks)"/>
    </g>
    <g role="img" aria-label="Aerial evening photo of a lit open-air market among trees">
      <polygon points="0,705 600,1115 0,1115" fill="url(#aerial)"/>
    </g>
    <polygon points="0,662 680,1115 600,1115 0,705" fill="var(--red)"/>
    <rect x="680" y="1085" width="180" height="30" fill="var(--red-deep)"/>
  </svg>

  <div class="brand"><span class="brand-mark"></span><span class="brand-name">BRAMWICK DEVELOPMENT</span></div>

  <h1 class="headline">CLIENT<br>JOURNEY TO<span class="accent">SUCCESS</span></h1>

  <section class="stage basecamp">
    <h2 class="stage-title">
      <svg class="badge" viewBox="0 0 44 48"><polygon points="22,2 41,13 41,35 22,46 3,35 3,13" fill="var(--red)" stroke="var(--paper)" stroke-width="2"/><polygon points="12,32 22,17 32,32" fill="none" stroke="var(--paper)" stroke-width="2"/></svg>
      Basecamp
    </h2>
    <ul class="stage-list">
      <li><svg class="tick" viewBox="0 0 12 12"><circle cx="6" cy="6" r="5" fill="none" stroke="var(--red)" stroke-width="1.2"/><path d="M3.5 6.2l1.8 1.8 3.4-3.6" fill="none" stroke="var(--red)" stroke-width="1.2"/></svg>Client Assessment</li>
      <li><svg class="tick" viewBox="0 0 12 12"><circle cx="6" cy="6" r="5" fill="none" stroke="var(--red)" stroke-width="1.2"/><path d="M3.5 6.2l1.8 1.8 3.4-3.6" fill="none" stroke="var(--red)" stroke-width="1.2"/></svg>Determine Project Goals</li>
      <li><svg class="tick" viewBox="0 0 12 12"><circle cx="6" cy="6" r="5" fill="none" stroke="var(--red)" stroke-width="1.2"/><path d="M3.5 6.2l1.8 1.8 3.4-3.6" fill="none" stroke="var(--red)" stroke-width="1.2"/></svg>Proposal &amp; Fees</li>
    </ul>
  </section>

  <section class="stage summit s1">
    <h2 class="stage-title">
      <svg class="badge" viewBox="0 0 44 48"><polygon points="22,2 41,13 41,35 22,46 3,35 3,13" fill="var(--ink)" stroke="var(--red)" stroke-width="2"/><polygon points="12,32 22,17 32,32" fill="none" stroke="var(--paper)" stroke-width="2"/></svg>
      <span class="summit-name">Summit 1<small>- PreConstruction</small></span>
    </h2>
    <ul class="stage-list">
      <li><svg class="tick" viewBox="0 0 12 12"><circle cx="6" cy="6" r="5" fill="none" stroke="var(--grey)" stroke-width="1"/><path d="M3.5 6.2l1.8 1.8 3.4-3.6" fill="none" stroke="var(--grey)" stroke-width="1"/></svg>Develop Project Plan</li>
      <li><svg class="tick" viewBox="0 0 12 12"><circle cx="6" cy="6" r="5" fill="none" stroke="var(--grey)" stroke-width="1"/><path d="M3.5 6.2l1.8 1.8 3.4-3.6" fill="none" stroke="var(--grey)" stroke-width="1"/></svg>Develop Risk Assessment &amp; Plan</li>
      <li><svg class="tick" viewBox="0 0 12 12"><circle cx="6" cy="6" r="5" fill="none" stroke="var(--grey)" stroke-width="1"/><path d="M3.5 6.2l1.8 1.8 3.4-3.6" fill="none" stroke="var(--grey)" stroke-width="1"/></svg>Devlelop Schedule</li>
      <li><svg class="tick" viewBox="0 0 12 12"><circle cx="6" cy="6" r="5" fill="none" stroke="var(--grey)" stroke-width="1"/><path d="M3.5 6.2l1.8 1.8 3.4-3.6" fill="none" stroke="var(--grey)" stroke-width="1"/></svg>Develop Budget</li>
      <li><svg class="tick" viewBox="0 0 12 12"><circle cx="6" cy="6" r="5" fill="none" stroke="var(--grey)" stroke-width="1"/><path d="M3.5 6.2l1.8 1.8 3.4-3.6" fill="none" stroke="var(--grey)" stroke-width="1"/></svg>Develop Team</li>
      <li><svg class="tick" viewBox="0 0 12 12"><circle cx="6" cy="6" r="5" fill="none" stroke="var(--grey)" stroke-width="1"/><path d="M3.5 6.2l1.8 1.8 3.4-3.6" fill="none" stroke="var(--grey)" stroke-width="1"/></svg>GC, Sub, Consultants Contracts</li>
    </ul>
  </section>

  <section class="stage summit s2">
    <h2 class="stage-title">
      <svg class="badge" viewBox="0 0 44 48"><polygon points="22,2 41,13 41,35 22,46 3,35 3,13" fill="var(--ink)" stroke="var(--red)" stroke-width="2"/><polygon points="12,32 22,17 32,32" fill="none" stroke="var(--paper)" stroke-width="2"/></svg>
      <span class="summit-name">Summit 2<small>- Execution</small></span>
    </h2>
    <ul class="stage-list">
      <li><svg class="tick" viewBox="0 0 12 12"><circle cx="6" cy="6" r="5" fill="none" stroke="var(--grey)" stroke-width="1"/><path d="M3.5 6.2l1.8 1.8 3.4-3.6" fill="none" stroke="var(--grey)" stroke-width="1"/></svg>Acquire Permits</li>
      <li><svg class="tick" viewBox="0 0 12 12"><circle cx="6" cy="6" r="5" fill="none" stroke="var(--grey)" stroke-width="1"/><path d="M3.5 6.2l1.8 1.8 3.4-3.6" fill="none" stroke="var(--grey)" stroke-width="1"/></svg>PreConstruction Meeting</li>
      <li><svg class="tick" viewBox="0 0 12 12"><circle cx="6" cy="6" r="5" fill="none" stroke="var(--grey)" stroke-width="1"/><path d="M3.5 6.2l1.8 1.8 3.4-3.6" fill="none" stroke="var(--grey)" stroke-width="1"/></svg>Project Start</li>
    </ul>
  </section>

  <section class="stage summit s3">
    <h2 class="stage-title">
      <svg class="badge" viewBox="0 0 44 48"><polygon points="22,2 41,13 41,35 22,46 3,35 3,13" fill="var(--ink)" stroke="var(--red)" stroke-width="2"/><polygon points="12,32 22,17 32,32" fill="none" stroke="var(--paper)" stroke-width="2"/></svg>
      <span class="summit-name">Summit 3<small>- Project Management</small></span>
    </h2>
    <ul class="stage-list">
      <li><svg class="tick" viewBox="0 0 12 12"><circle cx="6" cy="6" r="5" fill="none" stroke="var(--grey)" stroke-width="1"/><path d="M3.5 6.2l1.8 1.8 3.4-3.6" fill="none" stroke="var(--grey)" stroke-width="1"/></svg>Shared Consciousness Meetings</li>
      <li><svg class="tick" viewBox="0 0 12 12"><circle cx="6" cy="6" r="5" fill="none" stroke="var(--grey)" stroke-width="1"/><path d="M3.5 6.2l1.8 1.8 3.4-3.6" fill="none" stroke="var(--grey)" stroke-width="1"/></svg>Pressurized Collaboration</li>
      <li><svg class="tick" viewBox="0 0 12 12"><circle cx="6" cy="6" r="5" fill="none" stroke="var(--grey)" stroke-width="1"/><path d="M3.5 6.2l1.8 1.8 3.4-3.6" fill="none" stroke="var(--grey)" stroke-width="1"/></svg>Schedule Management</li>
      <li><svg class="tick" viewBox="0 0 12 12"><circle cx="6" cy="6" r="5" fill="none" stroke="var(--grey)" stroke-width="1"/><path d="M3.5 6.2l1.8 1.8 3.4-3.6" fill="none" stroke="var(--grey)" stroke-width="1"/></svg>Run O.O.D.A. Loop</li>
    </ul>
  </section>

  <section class="stage summit s4">
    <h2 class="stage-title">
      <svg class="badge" viewBox="0 0 44 48"><polygon points="22,2 41,13 41,35 22,46 3,35 3,13" fill="var(--ink)" stroke="var(--red)" stroke-width="2"/><polygon points="12,32 22,17 32,32" fill="none" stroke="var(--paper)" stroke-width="2"/></svg>
      <span class="summit-name">Summit 4<small>- Completion</small></span>
    </h2>
    <ul class="stage-list">
      <li><svg class="tick" viewBox="0 0 12 12"><circle cx="6" cy="6" r="5" fill="none" stroke="var(--grey)" stroke-width="1"/><path d="M3.5 6.2l1.8 1.8 3.4-3.6" fill="none" stroke="var(--grey)" stroke-width="1"/></svg>Closeout</li>
    </ul>
  </section>
</main>
</body>
</html>
```